One Page Sales Flyer for Wireless Survey- Computer Hardware

I want a designer to create a one page 4 color sales slick to be given to our sales team to sell to the end customers. I would like a visual picture of a heat map so vornix "heat map wireless" to get an idea of how that image should look.

```html
<!DOCTYPE html>
<html lang="en">
<head>
<meta charset="utf-8">
<title>Relaywise – Wireless Site Surveys</title>
<link href="https://fonts.googleapis.com/css2?family=Montserrat:wght@500;700;800&family=Raleway:wght@400;500&display=swap" rel="stylesheet">
<style>
  :root {
    --brand-blue: #3aa3dc;
    --ink: #2b2b2b;
    --charcoal: #333333;
    --panel: #f1f1f1;
    --dash: #9a9a9a;
    --white: #ffffff;
  }
  * { margin: 0; padding: 0; box-sizing: border-box; }
  html, body { width: 904px; height: 1200px; overflow: hidden; background: var(--white); }
  body { position: relative; font-family: "Raleway", sans-serif; color: var(--ink); }

  .brand { position: absolute; left: 39px; top: 25px; width: 180px; text-align: center; }
  .brand-mark { width: 84px; height: 84px; margin: 0 auto; border-radius: 10px; background: var(--brand-blue); }
  .brand-name { margin-top: 16px; font-family: "Montserrat", sans-serif; font-weight: 500; font-size: 27px; letter-spacing: 1px; color: var(--charcoal); }

  .headline {
    position: absolute; left: 279px; top: 23px; width: 625px; height: 136px;
    background: var(--brand-blue); border-radius: 26px 0 0 26px;
    display: flex; align-items: center; justify-content: center; text-align: center;
    font-family: "Montserrat", sans-serif; font-weight: 800; font-size: 35px; line-height: 37px; color: var(--white);
  }

  .intro-title {
    position: absolute; left: 37px; top: 241px; width: 320px;
    font-family: "Montserrat", sans-serif; font-weight: 800; font-size: 19px; line-height: 26px; color: var(--brand-blue);
  }
  .intro-rule { position: absolute; left: 37px; top: 295px; width: 66px; height: 2px; background: var(--ink); }
  .intro-text {
    position: absolute; left: 37px; top: 318px; width: 323px;
    font-size: 15.5px; line-height: 20.5px; text-align: justify;
  }

  .heatmap-visual {
    position: absolute; left: 394px; top: 195px; width: 486px; height: 332px;
    background: linear-gradient(135deg, #3a8fd1 0%, #5cc0a8 30%, #e8d84a 50%, #e8402e 65%, #8b5fb4 85%, #3b5aa8 100%);
    border-radius: 4px;
  }

  .section-pill {
    position: absolute; height: 31px; border-radius: 16px;
    display: flex; align-items: center; justify-content: center;
    font-family: "Montserrat", sans-serif; font-weight: 800; font-size: 19px; color: var(--white);
  }
  .pill-blue { background: var(--brand-blue); }
  .pill-dark { background: var(--charcoal); }
  .section-line { position: absolute; height: 2px; }

  .need-text {
    position: absolute; left: 37px; top: 597px; width: 831px;
    font-size: 15.5px; line-height: 20.5px; text-align: justify; text-align-last: center;
  }

  .benefits-box {
    position: absolute; left: 37px; top: 702px; width: 831px; height: 200px;
    background: var(--panel); border: 1.5px dashed var(--dash); border-radius: 16px;
  }
  .benefits-list { position: absolute; left: 42px; top: 733px; width: 808px; list-style: none; }
  .benefits-list li { position: relative; padding-left: 24px; font-size: 15.5px; line-height: 20.5px; text-align: justify; margin-bottom: 5px; }
  .benefits-list li::before {
    content: ""; position: absolute; left: 0; top: 6px; width: 10px; height: 10px; border-radius: 50%; background: var(--brand-blue);
  }

  .customer-list { position: absolute; top: 970px; list-style: none; }
  .customer-list li {
    position: relative; padding-left: 22px; height: 30px; line-height: 24px;
    font-family: "Montserrat", sans-serif; font-weight: 700; font-size: 16.5px; color: var(--brand-blue);
  }
  .customer-list li::before {
    content: ""; position: absolute; left: 0; top: 9px; width: 6px; height: 6px; border-radius: 50%; background: var(--brand-blue);
  }
  .customers-left { left: 161px; }
  .customers-right { left: 510px; }

  .footer-rule { position: absolute; left: 0; top: 1127px; width: 904px; height: 4px; background: var(--brand-blue); }
  .footer { position: absolute; left: 0; top: 1131px; width: 904px; height: 69px; background: var(--charcoal); }
  .contact {
    position: absolute; top: 1150px; display: flex; align-items: center; gap: 8px;
    font-family: "Montserrat", sans-serif; font-weight: 700; font-size: 18px; color: var(--white);
  }
  .contact svg { width: 22px; height: 22px; }
  .contact-email { left: 37px; }
  .contact-phone { left: 372px; }
  .contact-web {
    left: 627px; top: 1147px; width: 277px; height: 30px; padding-left: 8px;
    background: var(--white); border-radius: 15px 0 0 15px; color: var(--ink);
  }
</style>
</head>
<body>

  <div class="brand">
    <div class="brand-mark"></div>
    <div class="brand-name">RELAYWISE</div>
  </div>

  <h1 class="headline">INCREASE HARDWARE AND<br>SERVICES SPEND WITH<br>WIRELESS SITE SURVEYS</h1>

  <h2 class="intro-title">WHAT IS A WIRELESS SITE SURVEY OR HEAT MAP?</h2>
  <div class="intro-rule"></div>
  <p class="intro-text">A wireless site survey is a compilation of reports showing a visual representation of health of your wireless network. This does not only show how strong or weak a wireless signal is in any location it also helps aid in channel and placement to ensure maximum stable data rates are archived even where the single appears strong.</p>

  <div class="heatmap-visual" role="img" aria-label="Colour-coded world heat map with a legend of coloured zones"></div>

  <div class="section-line" style="left:144px; top:566px; width:616px; background:var(--brand-blue);"></div>
  <h2 class="section-pill pill-blue" style="left:184px; top:551px; width:532px;">WHY DO CUSTOMERS NEED A SITE SURVEY?</h2>
  <p class="need-text">Any variety of factors can contribute to an unhealthy wireless network (electrical, motors, materials used in construction, distance, neighboring wireless networks, etc.) and traditional methods that use only blueprints and a computer program to show signal strength have shown to be ineffective.</p>

  <div class="benefits-box"></div>
  <h2 class="section-pill pill-blue" style="left:271px; top:684px; width:360px;">WHY SHOULD THEY USE YOU?</h2>
  <ul class="benefits-list">
    <li>42% of businesses report some issues with wireless connectivity and acknowledge its effect on the bottom line*</li>
    <li>Most of these problems are solved through either fine tuning the current equipment (managed services) or purchasing new equipment (incremental sales) of which you can provide both</li>
    <li>Being a one-stop shop for all your customer’s IT needs prevents them from needing additional vendors</li>
    <li>The increase of IoT (Internet of things) and BYOD (Bring Your Own Device)</li>
  </ul>

  <div class="section-line" style="left:287px; top:936px; width:333px; background:var(--charcoal);"></div>
  <h2 class="section-pill pill-dark" style="left:318px; top:921px; width:270px;">TARGET CUSTOMERS</h2>
  <ul class="customer-list customers-left">
    <li>DISTRIBUTORS</li>
    <li>WAREHOUSES</li>
    <li>SLED</li>
    <li>K-12</li>
    <li>MEDICAL / HOSPITALS</li>
  </ul>
  <ul class="customer-list customers-right">
    <li>ENTERPRISE F1000</li>
    <li>SPORTS VENUES</li>
    <li>STADIUMS</li>
    <li>HOTELS</li>
    <li>RETAIL STORES</li>
  </ul>

  <div class="footer-rule"></div>
  <footer class="footer"></footer>
  <div class="contact contact-email">
    <svg viewBox="0 0 24 24"><circle cx="12" cy="12" r="12" fill="#3aa3dc"/><rect x="6" y="8" width="12" height="8.5" rx="1" fill="none" stroke="#fff" stroke-width="1.5"/><path d="M6.5 8.5 12 13l5.5-4.5" fill="none" stroke="#fff" stroke-width="1.5"/></svg>
    <span>hello@relaywise.com</span>
  </div>
  <div class="contact contact-phone">
    <svg viewBox="0 0 24 24"><circle cx="12" cy="12" r="12" fill="#3aa3dc"/><path d="M8.2 6.5c.5-.4 1.1-.3 1.4.2l1.2 2c.3.5.1 1-.3 1.3l-.7.5c.6 1.4 1.8 2.7 3.2 3.4l.5-.7c.3-.4.9-.6 1.3-.3l2 1.2c.5.3.6.9.2 1.4l-.9 1c-.6.6-1.5.8-2.3.4-2.9-1.3-5.2-3.6-6.5-6.5-.4-.8-.2-1.7.4-2.3z" fill="#fff"/></svg>
    <span>555-014-2290</span>
  </div>
  <div class="contact contact-web">
    <svg viewBox="0 0 24 24"><circle cx="12" cy="12" r="9" fill="none" stroke="#3aa3dc" stroke-width="1.6"/><ellipse cx="12" cy="12" rx="4" ry="9" fill="none" stroke="#3aa3dc" stroke-width="1.4"/><path d="M3 12h18M4.5 7.5h15M4.5 16.5h15" stroke="#3aa3dc" stroke-width="1.4"/></svg>
    <span>www.relaywise.com</span>
  </div>

</body>
</html>
```